Velvet Pressings Techno Label Business Card

I'm looking for a very clean business card for my Velvet Pressings music label. The label focusses on techno music. The card should include:

• my name : Bram Quintel as "Founder & CEO"
• email address: bram@velvet-pressings.example
• web: www.velvet-pressings.example
• facebook logo + /velvetpress
• twitter logo + /velvetpress
• soundcloud logo + /velvetpressings

Feel free to include your ideas! I'm looking forward to discuss about it.

Bram

Industry/Entity Type

Business

Contact Information for Business Card

I don't like glossy cards. Prefer matt.

Requirements
Nice to have
• Maybe on one side the complete logo, other side just the icon.
Should not have
• Flashy stuff. Must be clean and business like style.

```html
<!DOCTYPE html>
<html lang="en">
<head>
<meta charset="utf-8">
<title>Velvet Pressings — Business Card</title>
<link rel="stylesheet" href="https://fonts.googleapis.com/css2?family=Questrial&display=swap">
<style>
  :root {
    --backdrop: #dedbd6;
    --card-white: #f7f7f7;
    --card-shade: #e6e6e6;
    --band-grey: #8a8a8a;
    --ink-grey: #6f6f6f;
    --ink-dark: #4d4d4d;
    --accent: #f36f21;
    --on-band: #ffffff;
  }
  * { box-sizing: border-box; margin: 0; padding: 0; }
  html, body {
    width: 1200px;
    height: 900px;
    overflow: hidden;
    background: var(--backdrop);
    font-family: "Questrial", sans-serif;
  }
  .canvas {
    position: relative;
    width: 1200px;
    height: 900px;
  }
  .card {
    position: absolute;
    left: 290px;
    width: 620px;
    height: 354px;
    border-radius: 26px;
    overflow: hidden;
    background: linear-gradient(160deg, var(--card-white) 40%, var(--card-shade) 100%);
    box-shadow: 0 10px 24px rgba(0,0,0,0.18);
  }
  .card--front { top: 80px; }
  .card--back { top: 466px; }

  .front-band {
    position: absolute;
    inset: 0;
    width: 620px;
    height: 354px;
  }
  .holder {
    position: absolute;
    top: 34px;
    right: 40px;
    text-align: right;
    color: var(--on-band);
  }
  .holder__name {
    font-size: 21px;
    letter-spacing: 2px;
    text-transform: uppercase;
  }
  .holder__role {
    font-size: 14px;
    margin-top: 4px;
  }

  .contact-list {
    position: absolute;
    top: 140px;
    left: 34px;
    width: 230px;
    list-style: none;
    color: var(--ink-grey);
    font-size: 12px;
  }
  .contact-list li {
    display: flex;
    align-items: center;
    gap: 9px;
    height: 22px;
    white-space: nowrap;
  }
  .contact-list svg { width: 13px; height: 13px; flex: none; }
  .contact-list__dot {
    width: 11px;
    height: 11px;
    margin: 0 1px;
    border-radius: 50%;
    background: var(--accent);
    flex: none;
  }

  .wordmark {
    position: absolute;
    display: flex;
    align-items: center;
    gap: 12px;
    color: var(--ink-dark);
    font-size: 30px;
    letter-spacing: 0.5px;
    white-space: nowrap;
  }
  .wordmark__dot {
    width: 28px;
    height: 28px;
    border-radius: 50%;
    background: var(--accent);
    flex: none;
  }
  .card--front .wordmark { top: 200px; left: 300px; }
  .card--back .wordmark {
    top: 50%;
    left: 50%;
    transform: translate(-50%, -50%);
    font-size: 40px;
  }
  .card--back .wordmark__dot { width: 36px; height: 36px; }

  .address {
    position: absolute;
    right: 44px;
    bottom: 36px;
    text-align: right;
    font-size: 15px;
    font-style: normal;
    line-height: 1.5;
    color: var(--ink-dark);
  }
</style>
</head>
<body>
<main class="canvas">

  <section class="card card--front" aria-label="Business card front">
    <svg class="front-band" viewBox="0 0 620 354" aria-hidden="true">
      <path d="M0 0 H620 V150 Q330 40 0 40 Z" fill="var(--band-grey)"/>
      <path d="M0 54 Q330 54 620 166" fill="none" stroke="var(--accent)" stroke-width="4"/>
    </svg>

    <div class="holder">
      <p class="holder__name">Bram Quintel</p>
      <p class="holder__role">Founder &amp; CEO</p>
    </div>

    <ul class="contact-list">
      <li>
        <svg viewBox="0 0 16 16"><rect x="1" y="3" width="14" height="10" rx="1" fill="var(--accent)"/><path d="M1.5 3.5 L8 9 L14.5 3.5" fill="none" stroke="#fff" stroke-width="1.3"/></svg>
        <span>bram@velvet-pressings.example</span>
      </li>
      <li>
        <svg viewBox="0 0 16 16"><circle cx="8" cy="8" r="7" fill="var(--accent)"/><path d="M1 8 H15 M8 1 Q3 8 8 15 M8 1 Q13 8 8 15" fill="none" stroke="#fff" stroke-width="1"/></svg>
        <span>www.velvet-pressings.example</span>
      </li>
      <li>
        <span class="contact-list__dot"></span>
        <span>/velvetpress</span>
      </li>
      <li>
        <span class="contact-list__dot"></span>
        <span>/velvetpress</span>
      </li>
      <li>
        <span class="contact-list__dot"></span>
        <span>/velvetpressings</span>
      </li>
    </ul>

    <div class="wordmark">
      <span>Velvet Pressings</span>
      <span class="wordmark__dot"></span>
    </div>

    <address class="address">
      041 9th Floor Arcade<br>
      Halden Road LKG
    </address>
  </section>

  <section class="card card--back" aria-label="Business card back">
    <div class="wordmark">
      <span>Velvet Pressings</span>
      <span class="wordmark__dot"></span>
    </div>
  </section>

</main>
</body>
</html>
```